Locksmith, Safes, Security Systems, Camera Systems, Home Theater, Chip Keys & Remotes

Darnel Hoskins Owner
2871 Pemberly Vane Loop
Dothan, AL 36301
P 334-815-4092
F 334-527-3810
dhoskins@trevonmarts.com
www.trevonmarts.com
AL Lic #5827
*Maybe follow us on Facebook or Facebook symbol

```html
<!DOCTYPE html>
<html lang="en">
<head>
<meta charset="utf-8">
<title>Trevonmart's Lock &amp; Security — Darnel Hoskins</title>
<link href="https://fonts.googleapis.com/css2?family=Lato:wght@400;700&display=swap" rel="stylesheet">
<style>
  :root {
    --brand-blue: #2b3a8f;
    --card-cream: #eeede8;
    --ink: #111111;
    --white: #ffffff;
  }
  html, body {
    margin: 0;
    padding: 0;
    overflow: hidden;
    background: #ffffff;
  }
  .card {
    position: relative;
    width: 1200px;
    height: 702px;
    background: var(--brand-blue);
    font-family: 'Lato', Arial, sans-serif;
    overflow: hidden;
  }
  .card-face {
    position: absolute;
    left: 11px;
    top: 11px;
    width: 1178px;
    height: 680px;
    background: var(--card-cream);
  }
  .diagonal-band {
    position: absolute;
    left: 0;
    top: 0;
  }
  .brand {
    position: absolute;
    left: 44px;
    top: 42px;
    display: flex;
    align-items: center;
    gap: 40px;
  }
  .brand-mark {
    width: 135px;
    height: 194px;
    background: var(--brand-blue);
    border-radius: 6px;
  }
  .brand-name {
    color: var(--brand-blue);
    font-weight: 700;
    text-transform: uppercase;
    line-height: 1.1;
  }
  .brand-name .primary {
    display: block;
    font-size: 36px;
    letter-spacing: 0.5px;
  }
  .brand-name .secondary {
    display: block;
    font-size: 24px;
    letter-spacing: 1px;
    margin-top: 6px;
    padding-left: 40px;
  }
  .person {
    position: absolute;
    right: 66px;
    top: 70px;
    text-align: right;
  }
  .person-name {
    margin: 0;
    font-size: 54px;
    font-weight: 400;
    color: var(--ink);
    line-height: 1;
    letter-spacing: 0.5px;
  }
  .person-title {
    margin: 12px 0 0;
    font-size: 31px;
    color: var(--brand-blue);
    line-height: 1;
  }
  .person-license {
    margin: 10px 0 0;
    font-size: 17px;
    color: var(--ink);
  }
  .contact-row {
    position: absolute;
    right: 60px;
    display: flex;
    align-items: center;
    gap: 22px;
    color: var(--white);
    font-size: 26px;
    text-align: right;
    line-height: 1.4;
  }
  .contact-row .icon {
    width: 40px;
    display: flex;
    justify-content: center;
  }
  .row-address { top: 292px; }
  .row-phone { top: 364px; }
  .row-web { top: 458px; }
  .social {
    position: absolute;
    right: 60px;
    top: 608px;
    display: flex;
    align-items: center;
    gap: 22px;
    color: var(--white);
    font-size: 27px;
  }
  .social-dot {
    width: 30px;
    height: 30px;
    border-radius: 50%;
    background: var(--white);
  }
</style>
</head>
<body>
  <div class="card">
    <div class="card-face"></div>
    <svg class="diagonal-band" width="1200" height="702" viewBox="0 0 1200 702" aria-hidden="true">
      <polygon points="547,265 1189,265 1189,691 14,691" fill="var(--brand-blue)"/>
    </svg>

    <div class="brand">
      <div class="brand-mark"></div>
      <div class="brand-name">
        <span class="primary">Trevonmart's</span>
        <span class="secondary">Lock &amp; Security</span>
      </div>
    </div>

    <div class="person">
      <h1 class="person-name">DARNEL HOSKINS</h1>
      <p class="person-title">Owner</p>
      <p class="person-license">AL Lic #5827</p>
    </div>

    <div class="contact-row row-address">
      <div>2871 Pemberly Vane Loop Dothan, AL 36301</div>
      <div class="icon">
        <svg width="32" height="48" viewBox="0 0 32 48" aria-hidden="true">
          <path d="M16 0C7.2 0 0 7.2 0 16c0 12 16 32 16 32s16-20 16-32C32 7.2 24.8 0 16 0z" fill="var(--white)"/>
          <circle cx="16" cy="16" r="6" fill="var(--brand-blue)"/>
        </svg>
      </div>
    </div>

    <div class="contact-row row-phone">
      <div>P 334-815-4092<br>F 334-527-3810</div>
      <div class="icon">
        <svg width="26" height="42" viewBox="0 0 26 42" aria-hidden="true">
          <rect x="0" y="0" width="26" height="42" rx="4" fill="var(--white)"/>
          <rect x="3" y="5" width="20" height="28" fill="var(--brand-blue)"/>
          <circle cx="13" cy="37.5" r="2.2" fill="var(--brand-blue)"/>
        </svg>
      </div>
    </div>

    <div class="contact-row row-web">
      <div>dhoskins@trevonmarts.com<br>www.trevonmarts.com</div>
      <div class="icon">
        <svg width="38" height="28" viewBox="0 0 38 28" aria-hidden="true">
          <rect x="0" y="0" width="38" height="28" rx="3" fill="var(--white)"/>
          <path d="M1 3 L19 16 L37 3" fill="none" stroke="var(--brand-blue)" stroke-width="2.5"/>
        </svg>
      </div>
    </div>

    <div class="social">
      <span>Follow us on</span>
      <span class="social-dot" role="img" aria-label="Social network link"></span>
      <span class="social-dot" role="img" aria-label="Social network link"></span>
    </div>
  </div>
</body>
</html>
```